New IT recruitment and consulting company need web logo.

We need a web logo design for a new company based in Scandinavia called "Relmo".
We work with recruitment and management consulting within HR and strategy mainly for the IT industry in Scandinavia. Long experience from recruitment and the IT industry.
We would like to see designs that use the color orange. The design should communicate trust, enthusiasm, success and energy.

Target Market(s)

CEO and line managers in the potential customer companies.

Industry/Entity Type

Management Consulting

Number of Pages Required

1 page

Font styles to use
Sans Serif

Requirements
Must have
• Modern web design.
Nice to have
• We would like to see designs that use the color orange.

```html
<!DOCTYPE html>
<html lang="en">
<head>
<meta charset="utf-8">
<title>Relmo – Connecting Great People &amp; Great Organizations</title>
<link href="https://fonts.googleapis.com/css2?family=Poppins:wght@400;500;600&family=Lato:ital,wght@0,400;0,700;1,400&display=swap" rel="stylesheet">
<style>
:root{
  --orange:#f7941d;
  --orange-band:#fb9a1e;
  --ink:#1b1b1b;
  --text:#333333;
  --muted:#555555;
  --line:#c9c9c9;
  --panel-left:#e4e4e4;
  --panel-right:#ececec;
  --footer:#333333;
  --footer-bar:#1f1f1f;
  --footer-line:#555555;
  --white:#ffffff;
  --card-border:#8a8a8a;
  --tab:#7a7a7a;
}
*{box-sizing:border-box;margin:0;padding:0}
html,body{width:1200px;height:2329px;overflow:hidden}
body{position:relative;background:var(--white);font-family:"Lato",Arial,sans-serif;color:var(--text)}
.abs{position:absolute}
.head{font-family:"Poppins",Arial,sans-serif}

/* header */
.site-header{left:0;top:0;width:1200px;height:93px;background:#f8f8f8}
.brand{left:80px;top:8px;width:94px;height:94px;border-radius:50%;background:var(--white);border:5px solid var(--orange);z-index:3}
.brand-name{left:182px;top:34px;font:600 31px "Poppins",sans-serif;color:var(--orange);z-index:3}
.phone{left:950px;top:8px;display:flex;align-items:center;gap:10px;font:400 20px "Lato",sans-serif;color:var(--ink)}
.nav a{position:absolute;top:56px;font:700 14px "Lato",sans-serif;color:var(--ink);text-decoration:none;letter-spacing:.3px}
.nav a.active{left:582px;top:50px;width:70px;height:31px;background:var(--orange);color:var(--white);text-align:center;line-height:31px}

/* hero */
.hero{left:0;top:93px;width:1200px;height:488px;background:linear-gradient(90deg,#3b3a38 0%,#5a554f 35%,#8a8580 60%,#d8d5d2 80%,#efece9 100%)}
.hero-title{left:81px;top:250px;font:600 27px/37px "Poppins",sans-serif;color:var(--white);text-transform:uppercase;text-shadow:0 1px 3px rgba(0,0,0,.4)}
.dots span{position:absolute;top:385px;width:11px;height:11px;border-radius:50%;background:#d0d0d0}

/* section titles */
.section-title{left:0;width:1200px;text-align:center;font:600 34px "Poppins",sans-serif;color:var(--ink)}
.section-title em{font-style:normal;color:var(--orange)}
.rule{left:303px;width:594px;height:1px;background:var(--line)}
.rule-mark{left:588px;width:22px;height:22px;border-radius:50%;border:2px solid var(--orange);background:var(--white)}
.intro{left:0;top:720px;width:1200px;text-align:center;font:400 17px "Lato",sans-serif;color:var(--ink)}

/* services */
.service-band{left:0;top:983px;width:1200px;height:200px;background:var(--orange-band)}
.service-card{top:779px;width:326px;height:256px;border:3px solid var(--card-border)}
.service-photo{width:100%;height:100%}
.service-tab{top:984px;width:100px;height:51px;border-radius:50px 50px 0 0;background:var(--tab);display:flex;justify-content:center;padding-top:8px}
.service-name{top:1058px;width:326px;text-align:center;font:500 23px "Poppins",sans-serif;color:var(--white)}
.read-more{top:1108px;width:137px;height:35px;border-radius:18px;background:#111;border:2px solid var(--white);color:var(--white);font:700 13px "Lato",sans-serif;display:flex;align-items:center;padding-left:18px}
.read-more i{position:absolute;right:5px;top:4px;width:24px;height:24px;border-radius:50%;background:var(--white)}

/* testimonials / why */
.panel-left{left:0;top:1183px;width:595px;height:435px;background:linear-gradient(90deg,#ededed 0%,#e8e8e8 70%,#d9d9d9 100%)}
.panel-right{left:595px;top:1183px;width:605px;height:435px;background:var(--panel-right)}
.panel-title{top:1232px;font:500 29px "Poppins",sans-serif;color:var(--ink)}
.panel-title em{font-style:normal;color:var(--orange)}
.panel-rule{top:1281px;height:1px;background:var(--line)}
.avatar{left:81px;top:1323px;width:114px;height:114px;border-radius:50%;border:4px solid var(--orange);background:linear-gradient(160deg,#9fb8d0,#5d7893)}
.quote{left:225px;top:1322px;width:335px;font:italic 400 12.5px/20px "Lato",sans-serif;color:var(--ink)}
.quote b{font:700 26px/10px Georgia,serif;color:#999;vertical-align:-8px}
.person-rule{left:206px;top:1487px;width:226px;height:1px;background:var(--line)}
.person-name{left:206px;top:1507px;font:500 19px "Poppins",sans-serif;color:var(--orange)}
.person-role{left:206px;top:1536px;font:400 12.5px "Lato",sans-serif;color:var(--ink)}
.reason-line{left:657px;top:1330px;width:2px;height:190px;background:var(--orange)}
.reason-icon{left:634px;width:48px;height:48px;background:var(--panel-right);display:flex;align-items:center;justify-content:center}
.reason h3{font:700 19px "Lato",sans-serif;color:var(--ink);margin-bottom:6px}
.reason p{font:400 12.5px/21px "Lato",sans-serif;color:var(--muted);width:330px}

/* clients */
.client{top:1776px;width:151px;height:71px;border:1px solid #cfcfcf;display:flex;align-items:center;justify-content:center;gap:9px;font:400 21px "Lato",sans-serif;color:#333}
.client i{width:14px;height:14px;border-radius:50%;background:#444;display:block}
.arrow{top:1785px}

/* footer */
.footer-curve{left:0;top:1925px;width:1200px;height:404px}
.footer-mark{left:552px;top:1881px;width:94px;height:94px;border-radius:50%;background:var(--white);border:5px solid var(--orange);display:flex;align-items:center;justify-content:center;font:600 19px "Poppins",sans-serif;color:var(--orange)}
.col-title{top:2036px;font:500 19px "Poppins",sans-serif;color:var(--white)}
.col-title em{font-style:normal;color:var(--orange)}
.col-rule{top:2072px;height:1px;background:var(--footer-line)}
.col-divider{top:2060px;width:1px;height:190px;background:#444}
.links li{position:absolute;left:82px;list-style:none;font:400 12.5px "Lato",sans-serif;color:#ddd}
.contact-line{left:335px;font:400 12.5px/19px "Lato",sans-serif;color:#ddd}
.contact-line b{color:var(--white)}
.contact-icon{left:312px}
.field{left:640px;width:265px;height:35px;background:var(--white);font:400 12.5px "Lato",sans-serif;color:#333;padding:10px 12px}
.submit{left:640px;top:2222px;width:93px;height:34px;background:var(--orange);color:var(--white);font:700 17px "Lato",sans-serif;text-align:center;line-height:34px}
.social{left:1003px;display:flex;align-items:center;gap:12px;font:700 12.5px "Lato",sans-serif;color:var(--white)}
.social i{width:30px;height:30px;border-radius:50%;display:block}
.copyright{left:0;top:2285px;width:1200px;height:44px;background:var(--footer-bar);color:var(--white);text-align:center;font:700 12.5px/44px "Lato",sans-serif}
</style>
</head>
<body>

<header>
  <div class="abs site-header"></div>
  <div class="abs brand"></div>
  <div class="abs brand-name">RELMO</div>
  <div class="abs phone">
    <svg width="28" height="28" viewBox="0 0 28 28"><circle cx="14" cy="14" r="12.5" fill="none" stroke="#f7941d" stroke-width="2.5"/><path d="M10 8c1 0 2 2.5 2 3.2s-1.2 1-1 1.8c.5 1.6 2.3 3.6 4 4 .8.2 1.1-1 1.8-1s3.2 1 3.2 2-1.5 2.5-3 2.3C12.5 19.7 8.3 15.5 7.8 11 7.6 9.5 9 8 10 8z" fill="#f7941d"/></svg>
    555 014 2086
  </div>
  <nav class="nav">
    <a class="active" href="#">HOME</a>
    <a style="left:695px" href="#">ABOUT US</a>
    <a style="left:810px" href="#">SERVICES</a>
    <a style="left:924px" href="#">CAREER</a>
    <a style="left:1026px" href="#">CONTACT US</a>
  </nav>
</header>

<section>
  <div class="abs hero" role="img" aria-label="Smiling businesswoman working at a laptop in a bright office"></div>
  <h1 class="abs hero-title">Connecting great people<br>&amp; great organizations<br>together</h1>
  <div class="dots"><span style="left:81px;background:#f7941d"></span><span style="left:100px"></span><span style="left:119px"></span></div>
</section>

<section>
  <h2 class="abs section-title" style="top:622px">WELCOME TO <em>RELMO</em></h2>
  <div class="abs rule" style="top:686px"></div>
  <div class="abs rule-mark" style="top:675px"></div>
  <p class="abs intro">The Founders Of The Company Have Long Experience On The Expert Level Both From Recruitment And The IT Industry</p>

  <div class="abs service-band"></div>

  <div class="abs service-card" style="left:81px"><div class="service-photo" role="img" aria-label="Row of smiling job candidates seated in business attire" style="background:linear-gradient(135deg,#f2f2f2,#b8b0a8 60%,#5a5450)"></div></div>
  <div class="abs service-card" style="left:436px"><div class="service-photo" role="img" aria-label="Management team meeting around a laptop" style="background:linear-gradient(135deg,#e6e6e6,#8a8a8a 55%,#2e2e2e)"></div></div>
  <div class="abs service-card" style="left:792px"><div class="service-photo" role="img" aria-label="Hands reviewing charts and strategy documents" style="background:linear-gradient(135deg,#c8d6ea,#e8ecf2 50%,#7f9fc8)"></div></div>

  <div class="abs service-tab" style="left:194px"><svg width="34" height="34" viewBox="0 0 34 34" fill="none" stroke="#fff" stroke-width="2.5"><circle cx="17" cy="11" r="5"/><path d="M8 28c0-6 4-9 9-9s9 3 9 9"/><circle cx="6" cy="15" r="3"/><circle cx="28" cy="15" r="3"/></svg></div>
  <div class="abs service-tab" style="left:549px"><svg width="34" height="34" viewBox="0 0 34 34" fill="none" stroke="#fff" stroke-width="3"><circle cx="17" cy="17" r="6"/><path d="M17 3v5M17 26v5M3 17h5M26 17h5M7 7l3.5 3.5M23.5 23.5L27 27M27 7l-3.5 3.5M10.5 23.5L7 27"/></svg></div>
  <div class="abs service-tab" style="left:905px"><svg width="34" height="34" viewBox="0 0 34 34" fill="none" stroke="#fff" stroke-width="2.5"><circle cx="17" cy="17" r="13"/><circle cx="17" cy="17" r="7"/><path d="M17 17L30 4"/></svg></div>

  <h3 class="abs service-name" style="left:81px">IT RECRUITMENT</h3>
  <h3 class="abs service-name" style="left:436px">MANAGEMENT</h3>
  <h3 class="abs service-name" style="left:792px">HR &amp; STRATEGY</h3>

  <a class="abs read-more" style="left:175px">Read More<i><svg width="24" height="24" viewBox="0 0 24 24"><path d="M10 7l5 5-5 5" fill="none" stroke="#111" stroke-width="2.5"/></svg></i></a>
  <a class="abs read-more" style="left:530px">Read More<i><svg width="24" height="24" viewBox="0 0 24 24"><path d="M10 7l5 5-5 5" fill="none" stroke="#111" stroke-width="2.5"/></svg></i></a>
  <a class="abs read-more" style="left:885px">Read More<i><svg width="24" height="24" viewBox="0 0 24 24"><path d="M10 7l5 5-5 5" fill="none" stroke="#111" stroke-width="2.5"/></svg></i></a>
</section>

<section>
  <div class="abs panel-left"></div>
  <div class="abs panel-right"></div>

  <svg class="abs" style="left:82px;top:1238px" width="42" height="32" viewBox="0 0 42 32"><ellipse cx="15" cy="12" rx="14" ry="10" fill="#555"/><path d="M6 19l-3 8 9-5z" fill="#555"/><ellipse cx="28" cy="18" rx="12" ry="9" fill="#777"/><path d="M35 24l4 6-9-3z" fill="#777"/></svg>
  <h2 class="abs panel-title" style="left:140px">Client <em>Testimonials</em></h2>
  <div class="abs panel-rule" style="left:81px;width:475px"></div>

  <div class="abs avatar" role="img" aria-label="Portrait of a smiling client in a blue shirt"></div>
  <p class="abs quote"><b>“</b> Sed ut perspiciatis unde omnis iste natus error sit volup tatem accusantium doloremque laudantium, totam rem aperiam eaque ipsa quae ab illo inventore veritatis et quasi architecto beatae vitae dicta sunt explicabo. Nemo enim ipsam voluptatem quia voluptas sit aspernatur aut odit aut fugit, sed quia consequuntur magni dolores eos qui ratione voluptatem sequi nesciunt. Neque porro quisquam <b>”</b></p>
  <div class="abs person-rule"></div>
  <div class="abs person-name">Marcus Hallberg</div>
  <div class="abs person-role">Marketing Manager</div>

  <svg class="abs" style="left:630px;top:1238px" width="30" height="30" viewBox="0 0 30 30" fill="none"><rect x="2" y="6" width="20" height="20" stroke="#555" stroke-width="3"/><path d="M7 15l5 5 14-16" stroke="#555" stroke-width="3.5"/></svg>
  <h2 class="abs panel-title" style="left:672px">Why <em>Choose Us</em></h2>
  <div class="abs panel-rule" style="left:629px;width:489px"></div>

  <div class="abs reason-line"></div>
  <div class="abs reason-icon" style="top:1296px"><svg width="44" height="44" viewBox="0 0 44 44" fill="none" stroke="#f7941d" stroke-width="2"><path d="M22 4l16 8v18l-16 9-16-9V12z"/><path d="M6 12l16 9 16-9M22 21v18"/></svg></div>
  <div class="abs reason-icon" style="top:1391px"><svg width="44" height="44" viewBox="0 0 44 44"><rect x="4" y="6" width="34" height="24" fill="#f7941d"/><rect x="8" y="10" width="26" height="16" fill="#fff"/><circle cx="16" cy="17" r="4" fill="#f7941d"/><path d="M14 30l-4 10M28 30l4 10" stroke="#f7941d" stroke-width="3"/></svg></div>
  <div class="abs reason-icon" style="top:1486px"><svg width="44" height="44" viewBox="0 0 44 44" fill="none" stroke="#f7941d" stroke-width="3"><circle cx="24" cy="20" r="16"/><circle cx="24" cy="20" r="9"/><circle cx="24" cy="20" r="3" fill="#f7941d"/><path d="M24 20L6 38"/></svg></div>

  <div class="abs reason" style="left:694px;top:1306px"><h3>Our Modular Approach</h3><p>Lorem ipsum dolor sit amet, consectetuer adipiscing elit,<br>sed diam nonummy nibh euismod.</p></div>
  <div class="abs reason" style="left:694px;top:1402px"><h3>‘Hands-on’ Strategy</h3><p>Lorem ipsum dolor sit amet, consectetuer adipiscing elit,<br>sed diam nonummy nibh euismod.</p></div>
  <div class="abs reason" style="left:694px;top:1497px"><h3>Facilitate Decision-Making</h3><p>Lorem ipsum dolor sit amet, consectetuer adipiscing elit,<br>sed diam nonummy nibh euismod.</p></div>
</section>

<section>
  <h2 class="abs section-title" style="top:1659px">OUR <em>CLIENTS</em></h2>
  <div class="abs rule" style="top:1722px"></div>
  <div class="abs rule-mark" style="top:1711px"></div>

  <svg class="abs arrow" style="left:36px" width="24" height="50" viewBox="0 0 24 50"><path d="M20 2L4 25l16 23" fill="none" stroke="#c4c4c4" stroke-width="2"/></svg>
  <div class="abs client" style="left:81px"><i></i>Norvale</div>
  <div class="abs client" style="left:258px"><i></i>Kestrel</div>
  <div class="abs client" style="left:436px">Brightfold</div>
  <div class="abs client" style="left:613px">Lumen Grid</div>
  <div class="abs client" style="left:792px"><i></i>Norvale</div>
  <div class="abs client" style="left:969px">Haldor</div>
  <svg class="abs arrow" style="left:1140px" width="24" height="50" viewBox="0 0 24 50"><path d="M4 2l16 23L4 48" fill="none" stroke="#c4c4c4" stroke-width="2"/></svg>
</section>

<footer>
  <svg class="abs footer-curve" viewBox="0 0 1200 404" preserveAspectRatio="none"><path d="M0 85 Q600 -40 1200 85 V404 H0z" fill="#333333"/></svg>
  <div class="abs footer-mark">Relmo</div>

  <h4 class="abs col-title" style="left:82px">Quick <em>Links</em></h4>
  <div class="abs col-rule" style="left:82px;width:135px"></div>
  <ul class="links">
    <li style="top:2091px">• Home</li>
    <li style="top:2122px">• About Us</li>
    <li style="top:2153px">• Services</li>
    <li style="top:2184px">• Career</li>
    <li style="top:2215px">• Contact Us</li>
  </ul>
  <div class="abs col-divider" style="left:279px"></div>

  <h4 class="abs col-title" style="left:312px">Contact <em>Details</em></h4>
  <div class="abs col-rule" style="left:312px;width:244px"></div>
  <svg class="abs contact-icon" style="top:2090px" width="13" height="17" viewBox="0 0 13 17"><path d="M6.5 0C3 0 0 2.7 0 6.3 0 10.5 6.5 17 6.5 17S13 10.5 13 6.3C13 2.7 10 0 6.5 0z" fill="#f7941d"/><circle cx="6.5" cy="6.3" r="2.4" fill="#333"/></svg>
  <div class="abs contact-line" style="top:2089px"><b>RELMO</b><br>123, Ut wisi enim ad minim venia<br>Mor nostrni tation -123 456</div>
  <svg class="abs contact-icon" style="top:2170px" width="14" height="14" viewBox="0 0 14 14"><path d="M3 0c1 0 2 2.5 2 3.2S3.8 4.3 4 5c.6 1.8 2.5 3.7 4.2 4.2.8.2 1-1 1.8-1S14 9.5 14 10.5 12.5 14 11 13.8C5 13 .8 8.8 0 3 0 1.5 2 0 3 0z" fill="#f7941d"/></svg>
  <div class="abs contact-line" style="top:2166px"><b>555 014 2086</b></div>
  <svg class="abs contact-icon" style="top:2205px" width="15" height="14" viewBox="0 0 15 14"><rect x="3" y="0" width="9" height="4" fill="#f7941d"/><rect x="0" y="4" width="15" height="7" rx="1" fill="#f7941d"/><rect x="3" y="9" width="9" height="5" fill="#fff" stroke="#f7941d"/></svg>
  <div class="abs contact-line" style="top:2202px">555 014 2086</div>
  <svg class="abs contact-icon" style="top:2243px" width="15" height="11" viewBox="0 0 15 11"><rect width="15" height="11" fill="#f7941d"/><path d="M0 0l7.5 6L15 0" fill="none" stroke="#333" stroke-width="1.2"/></svg>
  <div class="abs contact-line" style="top:2238px">info@relmo.com</div>
  <div class="abs col-divider" style="left:590px"></div>

  <h4 class="abs col-title" style="left:640px">Quick <em>Contact</em></h4>
  <div class="abs col-rule" style="left:640px;width:265px"></div>
  <div class="abs field" style="top:2093px">Name</div>
  <div class="abs field" style="top:2136px">Email</div>
  <div class="abs field" style="top:2178px">Message</div>
  <div class="abs submit">Submit</div>
  <div class="abs col-divider" style="left:950px"></div>

  <h4 class="abs col-title" style="left:1003px">Follow <em>Us</em></h4>
  <div class="abs col-rule" style="left:1003px;width:115px"></div>
  <div class="abs social" style="top:2097px"><i style="background:#3b5998"></i>FRIENDSPACE</div>
  <div class="abs social" style="top:2140px"><i style="background:#29a9e1"></i>CHIRPER</div>
  <div class="abs social" style="top:2183px"><i style="background:#1a78b4"></i>PRONET</div>
  <div class="abs social" style="top:2227px"><i style="background:#dd4b39"></i>CIRCLEPLUS</div>

  <div class="abs copyright">Copyright © 2016 Relmo.&nbsp; All Rights Reserved.</div>
</footer>

</body>
</html>
```